Health Spectrum and Energy Slides

Create beautiful and facinating PowerPoint slides that inspire and motivate

Target Market(s)

Clients looking for strategic breakthroughs and transformation

Industry/Entity Type

Health

Requirements
Must have
• Beautiful, heartfelt and fascinating graphics.
Nice to have
• Award winning designs.

```html
<!DOCTYPE html>
<html lang="en">
<head>
<meta charset="utf-8">
<title>Charge Me UP! – Energy Use and Regeneration</title>
<link rel="stylesheet" href="https://fonts.googleapis.com/css2?family=Anton&family=Comfortaa:wght@300;400&family=Libre+Baskerville:wght@400;700&family=Open+Sans:wght@300;400;800&family=Roboto+Condensed:ital,wght@0,300;0,400;0,700;1,700&family=Roboto:wght@400&display=swap">
<style>
  :root {
    --bg: #ffffff;
    --title-blue: #1a8cf0;
    --ink: #222222;
    --energize-green: #1fbe1f;
    --energize-word: #4a4a4a;
    --energize-word-soft: #5c5c5c;
    --exhaust-red: #e41010;
    --exhaust-word: #ef8080;
    --arrow-green: #1aa84a;
    --arrow-red: #e01b24;
    --figure-tone: #e9d9c4;
    --band-yellow: #fbe9a6;
    --band-orange: #d9a46a;
  }
  html, body { margin: 0; padding: 0; overflow: hidden; background: var(--bg); }
  .slide {
    position: relative;
    width: 1200px;
    height: 720px;
    overflow: hidden;
    background: var(--bg);
    font-family: "Roboto", sans-serif;
  }
  .slide * { margin: 0; white-space: nowrap; line-height: 1; }
  .abs { position: absolute; }

  .title {
    left: 0; width: 1264px; top: 44px; text-align: center;
    font-family: "Roboto Condensed", sans-serif; font-weight: 400;
    font-size: 56px; color: var(--title-blue);
  }
  .subtitle {
    left: 0; width: 1264px; top: 104px; text-align: center;
    font-family: "Roboto Condensed", sans-serif; font-weight: 400;
    font-size: 28px; color: var(--ink);
  }
  .column-head {
    top: 104px; font-family: "Roboto Condensed", sans-serif;
    font-weight: 400; font-size: 52px;
  }
  .column-head--energize { left: 102px; color: var(--energize-green); }
  .column-head--exhaust { left: 922px; color: var(--exhaust-red); }

  .energize-word { color: var(--energize-word); }
  .exhaust-word { color: var(--exhaust-word); }

  .w-round { font-family: "Comfortaa", sans-serif; font-weight: 300; }
  .w-sans { font-family: "Open Sans", sans-serif; font-weight: 400; }
  .w-sans-light { font-family: "Open Sans", sans-serif; font-weight: 300; }
  .w-heavy { font-family: "Open Sans", sans-serif; font-weight: 800; }
  .w-cond { font-family: "Roboto Condensed", sans-serif; font-weight: 400; }
  .w-cond-light { font-family: "Roboto Condensed", sans-serif; font-weight: 300; }
  .w-cond-bold { font-family: "Roboto Condensed", sans-serif; font-weight: 700; }
  .w-cond-bold-italic { font-family: "Roboto Condensed", sans-serif; font-weight: 700; font-style: italic; }
  .w-serif { font-family: "Libre Baskerville", serif; font-weight: 400; }
  .w-serif-bold { font-family: "Libre Baskerville", serif; font-weight: 700; }
  .w-block { font-family: "Anton", sans-serif; font-weight: 400; }

  .figure {
    border-radius: 10px;
    background: radial-gradient(ellipse at 50% 40%, var(--figure-tone), #f6efe6 70%, #ffffff);
  }
  .figure--energized { left: 452px; top: 188px; width: 136px; height: 250px; }
  .figure--drained { left: 688px; top: 164px; width: 112px; height: 276px; }

  .energy-words {
    left: 350px; width: 600px; top: 612px; text-align: center;
    font-size: 13.5px; line-height: 18px; color: #111;
  }
  .energy-words p { line-height: 18px; }

  .footer-band {
    left: 0; top: 716px; width: 1200px; height: 4px;
    background: linear-gradient(90deg, var(--band-yellow) 0%, var(--band-yellow) 64%, var(--band-orange) 65%, #c47a44 100%);
  }
</style>
</head>
<body>
<main class="slide">
  <h1 class="abs title">Charge Me UP!</h1>
  <p class="abs subtitle">Energy Use and Regeneration</p>

  <h2 class="abs column-head column-head--energize">Energize</h2>
  <h2 class="abs column-head column-head--exhaust">Exhaust</h2>

  <!-- Energize word cloud -->
  <div class="energize-cloud">
    <span class="abs energize-word w-round" style="left:62px;top:178px;font-size:31px;color:#333">Love &amp; Loved</span>
    <span class="abs energize-word w-round" style="left:90px;top:208px;font-size:23px">Heartfelt Breating</span>
    <span class="abs energize-word w-heavy" style="left:56px;top:231px;font-size:22px">Gratitude</span>
    <span class="abs energize-word w-sans" style="left:194px;top:231px;font-size:23px">Action</span>
    <span class="abs energize-word w-heavy" style="left:109px;top:256px;font-size:21px">Authentic Awe</span>
    <span class="abs energize-word w-heavy" style="left:157px;top:280px;font-size:22px">CARING</span>
    <span class="abs energize-word w-cond-bold" style="left:59px;top:304px;font-size:27px">CARED FOR COMMITMENT</span>
    <span class="abs energize-word w-serif" style="left:72px;top:335px;font-size:21px">Let Go i Don’t Control</span>
    <span class="abs energize-word w-serif" style="left:72px;top:365px;font-size:21px">Others Lifeline Session</span>
    <span class="abs energize-word w-serif-bold" style="left:126px;top:390px;font-size:20px">Meditation</span>
    <span class="abs energize-word w-serif-bold" style="left:168px;top:418px;font-size:19px">Nature</span>
    <span class="abs energize-word w-serif-bold" style="left:90px;top:441px;font-size:19px">Oneness</span>
    <span class="abs energize-word w-serif-bold" style="left:183px;top:439px;font-size:38px">Source</span>
    <span class="abs energize-word w-sans" style="left:108px;top:470px;font-size:21px">GOD</span>
    <span class="abs energize-word w-sans" style="left:166px;top:470px;font-size:33px">Pray</span>
    <span class="abs energize-word w-sans" style="left:59px;top:494px;font-size:25px">Progress</span>
    <span class="abs energize-word w-sans" style="left:166px;top:505px;font-size:30px">Patience</span>
    <span class="abs energize-word w-sans" style="left:82px;top:535px;font-size:17px">Positive + Surprise</span>
    <span class="abs energize-word w-sans" style="left:102px;top:550px;font-size:21px">Peace</span>
    <span class="abs energize-word w-heavy" style="left:168px;top:551px;font-size:21px">Responsible</span>
    <span class="abs energize-word w-sans" style="left:70px;top:572px;font-size:17px">See Potential</span>
    <span class="abs energize-word w-cond-bold" style="left:181px;top:577px;font-size:20px">See Opportunity</span>
    <span class="abs energize-word w-cond-bold" style="left:91px;top:596px;font-size:19px">Student Mindset</span>
    <span class="abs energize-word w-cond-bold" style="left:231px;top:603px;font-size:26px">Sleep</span>
    <span class="abs energize-word w-cond-bold" style="left:77px;top:627px;font-size:28px">Values Centered Action</span>
  </div>

  <!-- Exhaust word cloud -->
  <div class="exhaust-cloud">
    <span class="abs exhaust-word w-cond" style="left:908px;top:177px;font-size:27px">Anger</span>
    <span class="abs exhaust-word w-cond" style="left:974px;top:176px;font-size:36px">Anxiety</span>
    <span class="abs exhaust-word w-block" style="left:908px;top:208px;font-size:38px">Blame</span>
    <span class="abs exhaust-word w-sans" style="left:1024px;top:222px;font-size:26px">Compare</span>
    <span class="abs exhaust-word w-sans" style="left:950px;top:248px;font-size:24px">Need Control</span>
    <span class="abs exhaust-word w-sans-light" style="left:906px;top:264px;font-size:34px">Envy</span>
    <span class="abs exhaust-word w-heavy" style="left:987px;top:273px;font-size:29px">Entitlement</span>
    <span class="abs exhaust-word w-cond" style="left:936px;top:306px;font-size:19px">Expect The Worst</span>
    <span class="abs exhaust-word w-cond" style="left:1095px;top:305px;font-size:42px">Fear</span>
    <span class="abs exhaust-word w-cond" style="left:958px;top:323px;font-size:28px">Frustration</span>
    <span class="abs exhaust-word w-cond-bold" style="left:922px;top:350px;font-size:27px">Greed</span>
    <span class="abs exhaust-word w-sans-light" style="left:1002px;top:350px;font-size:46px">Lack</span>
    <span class="abs exhaust-word w-cond-bold-italic" style="left:1110px;top:360px;font-size:27px">Mask</span>
    <span class="abs exhaust-word w-sans" style="left:925px;top:396px;font-size:27px">Negative Surprise</span>
    <span class="abs exhaust-word w-cond-bold-italic" style="left:1006px;top:427px;font-size:28px">Want More</span>
    <span class="abs exhaust-word w-sans" style="left:928px;top:453px;font-size:27px">Procrastinate</span>
    <span class="abs exhaust-word w-heavy" style="left:984px;top:479px;font-size:25px">Resentment</span>
    <span class="abs exhaust-word w-sans" style="left:937px;top:499px;font-size:33px">Shame</span>
    <span class="abs exhaust-word w-block" style="left:1048px;top:508px;font-size:38px">Victim</span>
    <span class="abs exhaust-word w-sans-light" style="left:957px;top:540px;font-size:47px">Why Me</span>
  </div>

  <!-- Figures -->
  <div class="abs figure figure--energized" role="img" aria-label="Cartoon businessman jumping for joy, fully energized"></div>
  <div class="abs figure figure--drained" role="img" aria-label="Cartoon businessman with crossed arms and question marks overhead, drained and confused"></div>

  <!-- Direction arrows -->
  <svg class="abs" style="left:424px;top:388px" width="16" height="118" viewBox="0 0 16 118" aria-hidden="true">
    <line x1="8" y1="10" x2="8" y2="116" stroke="var(--arrow-green)" stroke-width="2.5"/>
    <polygon points="8,0 3,11 13,11" fill="var(--arrow-green)"/>
  </svg>
  <svg class="abs" style="left:821px;top:386px" width="16" height="112" viewBox="0 0 16 112" aria-hidden="true">
    <line x1="8" y1="0" x2="8" y2="100" stroke="var(--arrow-red)" stroke-width="2.5"/>
    <polygon points="8,111 3,100 13,100" fill="var(--arrow-red)"/>
  </svg>

  <!-- Battery levels -->
  <svg class="abs battery-levels" style="left:496px;top:458px" width="256" height="142" viewBox="0 0 256 142" role="img" aria-label="Four batteries draining from full green to low red">
    <defs>
      <linearGradient id="casing" x1="0" x2="1">
        <stop offset="0" stop-color="#d8d8d8"/>
        <stop offset="0.45" stop-color="#f7f7f7"/>
        <stop offset="1" stop-color="#bdbdbd"/>
      </linearGradient>
    </defs>
    <g class="battery">
      <rect x="24" y="3" width="14" height="9" rx="2" fill="#222"/>
      <rect x="4" y="11" width="56" height="128" rx="6" fill="url(#casing)" stroke="#9a9a9a"/>
      <rect x="9" y="18" width="46" height="25" rx="3" fill="#22c322"/>
      <rect x="9" y="47" width="46" height="25" rx="3" fill="#22c322"/>
      <rect x="9" y="76" width="46" height="25" rx="3" fill="#22c322"/>
      <rect x="9" y="105" width="46" height="25" rx="3" fill="#22c322"/>
    </g>
    <g class="battery" transform="translate(63 0)">
      <rect x="24" y="3" width="14" height="9" rx="2" fill="#222"/>
      <rect x="4" y="11" width="56" height="128" rx="6" fill="url(#casing)" stroke="#9a9a9a"/>
      <rect x="9" y="47" width="46" height="25" rx="3" fill="#e3b812"/>
      <rect x="9" y="76" width="46" height="25" rx="3" fill="#e3b812"/>
      <rect x="9" y="105" width="46" height="25" rx="3" fill="#e3b812"/>
    </g>
    <g class="battery" transform="translate(126 0)">
      <rect x="24" y="3" width="14" height="9" rx="2" fill="#222"/>
      <rect x="4" y="11" width="56" height="128" rx="6" fill="url(#casing)" stroke="#9a9a9a"/>
      <rect x="9" y="76" width="46" height="25" rx="3" fill="#ef6b14"/>
      <rect x="9" y="105" width="46" height="25" rx="3" fill="#ef6b14"/>
    </g>
    <g class="battery" transform="translate(189 0)">
      <rect x="24" y="3" width="14" height="9" rx="2" fill="#222"/>
      <rect x="4" y="11" width="56" height="128" rx="6" fill="url(#casing)" stroke="#9a9a9a"/>
      <rect x="9" y="109" width="46" height="21" rx="3" fill="#e0141c"/>
    </g>
  </svg>

  <div class="abs energy-words">
    <p>Awareness Aligned Balance Clear Conscious Capacity</p>
    <p>Creative Co-Create Choice Determined Disciplined Ease Flexible Focus Flow,</p>
    <p>presence Resilient Recovery Rebound Replenish Renew Sleep</p>
    <p>Strong Stable Willpower Leaks Weak Drain</p>
  </div>

  <div class="abs footer-band" aria-hidden="true"></div>
</main>
</body>
</html>
```